Box Design for Flooring product

***IMPORTANT: PLEASE READ THE DOCUMENT PROVIDED WITH THIS BRIEF CAREFULLY BEFORE ACCEPTING THIS PROJECT***
Need a creative design for the packaging of a flooring product. The packaging is two boxes: one holding 36 planks of flooring, and the other 7 planks of flooring. There are 4 colours for the flooring planks that need a box designed (for both the 36 plank box and 7 plank box). The boxes measures 92 cm x 16cm x 7cm (36 planks) and 92 cm x 16cm x 1.5cm (7 planks).
More details are provided in the requirements document attached with this brief. Also attaching other supporting documents with this brief mentioned in the document.
Need extra days to review
- Montserrat-Regular

```html
<!DOCTYPE html>
<html lang="en">
<head>
<meta charset="utf-8">
<title>Veradon Self Adhesive Vinyl Planks – 7 Plank Box</title>
<link href="https://fonts.googleapis.com/css2?family=Montserrat:wght@400;500;600;700;800&display=swap" rel="stylesheet">
<style>
:root{
  --olive:#4b4d3a;
  --white:#ffffff;
  --ink:#2b2b26;
  --line:#c9c9c9;
  --oak:#e4e8e4;
}
*{margin:0;padding:0;box-sizing:border-box}
html,body{width:1200px;height:1000px;overflow:hidden;background:#fff;font-family:"Montserrat",sans-serif;color:var(--ink)}
.canvas{position:relative;width:1200px;height:1000px;overflow:hidden}
.dieline{position:absolute;left:-110px;top:120px;width:1410px;height:700px}
.shapes{position:absolute;left:0;top:0}
.brand{position:absolute;display:flex;align-items:center;gap:9px;color:var(--white)}
.brand-mark{width:18px;height:18px;background:var(--white)}
.brand-name{font-weight:500;font-size:25px;letter-spacing:1.5px;line-height:1}
.brand-tag{position:absolute;color:var(--white);font-size:6.5px;letter-spacing:2.6px;font-weight:500}
.title{position:absolute;color:var(--white);font-weight:700;line-height:1.02}
.subtitle{position:absolute;color:var(--white);font-size:13.5px;font-weight:400}

.instructions{position:absolute;left:472px;top:194px;width:393px;height:166px;background:var(--white);border-radius:6px;padding:5px 6px}
.instructions h4{font-size:5.5px;font-weight:700;margin-bottom:2px}
.cols{display:flex;gap:5px}
.col{width:125px}
.step{display:flex;gap:3px;margin-bottom:4px}
.step .thumb{flex:0 0 22px;height:22px;border-radius:2px;background:linear-gradient(135deg,#d9c39a,#8d8e80)}
.step b{display:block;font-size:3.8px;font-weight:700;margin-bottom:1px}
.step p{font-size:3.6px;line-height:1.25}

.producer{position:absolute;right:302px;top:199px;text-align:right;font-size:7px;line-height:1.2}
.producer strong{font-weight:700}
.cert{position:absolute;left:1002px;top:264px;width:107px;border:1.5px solid var(--ink);font-size:4.8px}
.cert .mark{height:34px;display:flex;align-items:center;justify-content:center;border-bottom:1px solid var(--ink)}
.cert .mark span{width:36px;height:22px;border:2px solid var(--ink);border-radius:3px}
.cert .row{display:flex;justify-content:space-between;padding:1px 3px;border-bottom:1px solid var(--ink);font-weight:700}
.cert .row:last-child{border-bottom:none}
.cert .center{justify-content:center;text-align:center;font-weight:600}

.count-band{position:absolute;background:var(--olive);color:var(--white);text-align:center;font-weight:700}
.count-band .num{font-weight:800}
.coverage{position:absolute;font-weight:600;color:var(--ink);white-space:nowrap}
.size-box{position:absolute;border:1.5px solid var(--olive);text-align:right;color:var(--ink);white-space:nowrap}
.size-box span{display:block}
.size-box small{font-size:.62em}
.size-box .approx{font-size:.7em;line-height:1}
.barcode-box{position:absolute;left:1119px;top:301px;width:110px;height:53px;border:1.5px solid var(--ink);display:flex;align-items:center;justify-content:center;font-weight:700;font-size:13px;letter-spacing:.3px}

.features{position:absolute;left:590px;top:406px;display:flex;gap:10px}
.feature{width:55px;text-align:center}
.feature .icon{width:55px;height:52px;border:2px solid var(--white);border-radius:5px}
.feature span{display:block;color:var(--white);font-size:5.5px;line-height:1.15;margin-top:3px}
.shade{position:absolute;left:1038px;top:527px;width:200px;height:40px;border:4px solid var(--olive);border-radius:6px;background:var(--oak);font-size:14px;color:var(--olive);padding:8px 6px;letter-spacing:.3px}
</style>
</head>
<body>
<div class="canvas">
 <div class="dieline">
  <svg class="shapes" width="1410" height="700" viewBox="0 0 1410 700">
   <defs>
    <linearGradient id="roomTone" x1="0" y1="0" x2="0" y2="1">
     <stop offset="0" stop-color="#eef0ee"/>
     <stop offset=".45" stop-color="#d7dbd8"/>
     <stop offset="1" stop-color="#c4cac7"/>
    </linearGradient>
   </defs>
   <path d="M150 172 L160 165 L1258 165 L1270 172 L1270 580 L1258 595 L160 595 L150 580 Z" fill="none" stroke="#bdbdbd" stroke-width="1"/>
   <line x1="150" y1="387" x2="1270" y2="387" stroke="#bdbdbd" stroke-width="1"/>
   <polygon points="165,183 958,183 868,370 165,370" fill="var(--olive)"/>
   <polygon points="972,183 994,183 904,370 882,370" fill="var(--olive)"/>
   <polygon points="1003,183 1024,183 934,370 913,370" fill="var(--olive)"/>
   <rect x="790" y="390" width="272" height="187" fill="url(#roomTone)" role="img" aria-label="Interior photo: white oak vinyl floor with wooden chairs by a window"/>
   <polygon points="165,390 822,390 732,577 165,577" fill="var(--olive)"/>
   <polygon points="835,390 852,390 762,577 745,577" fill="var(--olive)"/>
   <polygon points="862,390 880,390 790,577 772,577" fill="var(--olive)"/>
   <polygon points="860,430 935,577 785,577" fill="var(--olive)"/>
   <polygon points="860,468 910,568 810,568" fill="var(--white)"/>
  </svg>

  <div class="brand" style="left:190px;top:203px"><span class="brand-mark"></span><span class="brand-name">VERADON</span></div>
  <div class="brand-tag" style="left:238px;top:228px">PREMIUM FLOORS AND TILES</div>
  <div class="title" style="left:190px;top:285px;font-size:25px">SELF ADHESIVE<br>VINYL PLANKS</div>
  <div class="subtitle" style="left:190px;top:338px">Suitable for general domestic use</div>

  <div class="instructions">
   <h4>Installation instructions</h4>
   <div class="cols">
    <div class="col">
     <div class="step"><div class="thumb" role="img" aria-label="Tools needed"></div><div><b>Step 1 - Tools Needed</b><p>Utility knife, tape measure, pencil, straight edge, clean cloth</p></div></div>
     <div class="step"><div class="thumb" role="img" aria-label="Planks acclimatising"></div><div><b>Step 2 - Acclimatise your floor</b><p>Store unopened packs in the room for 24 hours before laying.</p></div></div>
     <div class="step"><div class="thumb" role="img" aria-label="Removing skirting"></div><div><b>Step 3 - Removing Skirting board</b><p>Carefully remove skirting boards in the room.</p></div></div>
     <div class="step"><div class="thumb" role="img" aria-label="Marking layout"></div><div><b>Step 4 - Planning your layout</b><p>Find the centre of the room and mark two guide lines.</p></div></div>
    </div>
    <div class="col">
     <div class="step"><div class="thumb" role="img" aria-label="Cleaning floor"></div><div><b>Step 5 - Get ready to lay</b><p>Make sure the floor is clean, dry, flat and free of dust.</p></div></div>
     <div class="step"><div class="thumb" role="img" aria-label="Dry laying planks"></div><div><b>Step 6 - Dry lay your planks</b><p>Lay a row without peeling to check the pattern and fit.</p></div></div>
     <div class="step"><div class="thumb" role="img" aria-label="Arrows on backing"></div><div><b>Step 7 - Arrows on the backing paper</b><p>Keep all arrows pointing the same way.</p></div></div>
     <div class="step"><div class="thumb" role="img" aria-label="Laying first plank"></div><div><b>Step 8 - Laying the first plank</b><p>Peel the backing and press firmly along the guide line.</p></div></div>
    </div>
    <div class="col">
     <div class="step"><div class="thumb" role="img" aria-label="Laying planks"></div><div><b>Step 9 - Laying the remaining planks</b><p>Continue row by row, staggering the joints by at least 15 cm.</p></div></div>
     <div class="step"><div class="thumb" role="img" aria-label="Cutting planks"></div><div><b>Step 10 - Cutting the planks</b><p>Score the face with a knife against a straight edge.</p></div></div>
     <div class="step"><div class="thumb" role="img" aria-label="Breaking cut plank"></div><div><b>Step 11 - Breaking the cut plank</b><p>Bend along the score line until it snaps.</p></div></div>
     <div class="step"><div class="thumb" role="img" aria-label="Fitting cut planks"></div><div><b>Step 12 - Laying the cut planks</b><p>Fit cut pieces at the walls, then refit skirting boards.</p></div></div>
    </div>
   </div>
  </div>

  <div class="producer"><strong>Produced by :</strong><br>Veradon<br>Sample address, Unit #<br>City, 12345<br>www.veradonfloors.example<br><strong>Costumer Service :</strong><br>555-014-2290</div>

  <div class="cert">
   <div class="mark"><span></span></div>
   <div class="row center">Veradon™<br>Premium Floors and Tiles</div>
   <div class="row center">EN 14041, EN 13501-1, EN 717-1, EN 13893</div>
   <div class="row"><span>Reaction to Fire</span><span>Bfl-S1</span></div>
   <div class="row"><span>Emission of Formaldehyde</span><span>E1</span></div>
   <div class="row"><span>Slipperiness</span><span>DS</span></div>
  </div>

  <div class="count-band" style="left:1118px;top:201px;width:133px;height:29px;font-size:11px;line-height:29px"><span class="num" style="font-size:22px">7</span> Planks</div>
  <div class="coverage" style="left:1119px;top:233px;font-size:10.5px">Pack coverage 1 m²</div>
  <div class="size-box" style="left:1120px;top:248px;width:108px;font-size:8px;line-height:1.05;padding:2px 4px 3px">
   <span>Plank Size :</span><span>914 mm x 152 mm</span><span class="approx">(36" x 6" approx.)</span><span>1.8 mm <small>(0.07")</small> Thickness</span>
  </div>
  <div class="barcode-box">BARCODE</div>

  <div class="brand" style="left:190px;top:410px"><span class="brand-mark"></span><span class="brand-name">VERADON</span></div>
  <div class="brand-tag" style="left:238px;top:435px">PREMIUM FLOORS AND TILES</div>
  <div class="features">
   <div class="feature"><div class="icon" role="img" aria-label="Easy to lay illustration" style="background:linear-gradient(135deg,#e8e4d2,#c7c2a4)"></div><span>Easy to lay</span></div>
   <div class="feature"><div class="icon" role="img" aria-label="Water resistant illustration" style="background:linear-gradient(135deg,#6cc7d6,#e89a3c)"></div><span>Water resistant,<br>easy to clean</span></div>
   <div class="feature"><div class="icon" role="img" aria-label="Bathroom and kitchen illustration" style="background:linear-gradient(135deg,#f5c6a5,#8fd6de)"></div><span>Ideal for Bathrooms<br>and Kitchens</span></div>
  </div>
  <div class="title" style="left:190px;top:505px;font-size:31.5px">SELF ADHESIVE VINYL PLANKS</div>
  <div class="subtitle" style="left:190px;top:542px">Suitable for general domestic use</div>

  <div class="count-band" style="left:1068px;top:407px;width:184px;height:30px;font-size:14px;line-height:32px"><span class="num" style="font-size:25px">7</span> Planks</div>
  <div class="coverage" style="left:1077px;top:441px;font-size:14px">Pack coverage 1 m²</div>
  <div class="size-box" style="left:1068px;top:464px;width:159px;font-size:12px;line-height:1.0;padding:3px 5px 3px">
   <span>Plank Size :</span><span>914 mm x 152 mm</span><span class="approx">(36" x 6" approx.)</span><span>1.8 mm <small>(0.07")</small> Thickness</span>
  </div>
  <div class="shade">WHITE OAK</div>
 </div>
</div>
</body>
</html>
```